Onboarding project UI redesign

The web site is used to onboard clients via a video-identification process.
The end-user first tests his computer, then enters his order details and waits for an operator engagement.
When the operator engages the customer, they go through some identification steps together, ending on a contract signature page.

Target Market(s)

Finance B2C

Industry/Entity Type

Finance

Coding

Coded - Design and coding required

Number of Pages Required

5+ page

Font styles to use
Sans Serif

Requirements
Must have
• Professional UI
• Design for mobile devices

```html
<!DOCTYPE html>
<html lang="en">
<head>
<meta charset="utf-8">
<title>Waiting for operator – Novia Bank onboarding</title>
<link rel="stylesheet" href="https://fonts.googleapis.com/css2?family=Roboto:wght@300;400;500&display=swap">
<style>
  :root {
    --page-bg: #f8f9fc;
    --surface: #ffffff;
    --divider: #eceef3;
    --accent: #1a7ef5;
    --accent-soft: #c9def9;
    --step-idle: #e6ecf6;
    --step-idle-text: #ffffff;
    --title: #4f5f8f;
    --body-text: #5a5d66;
    --brand: #1e4a86;
    --footer-text: #c3c6cf;
  }
  * { box-sizing: border-box; margin: 0; padding: 0; }
  html, body {
    width: 1200px; height: 634px; overflow: hidden;
    background: var(--page-bg);
    font-family: "Roboto", Arial, sans-serif;
  }
  .screen { position: relative; width: 1200px; height: 634px; }

  .stepper {
    position: absolute; left: 0; top: 0; width: 1200px; height: 55px;
    background: var(--surface);
    border-bottom: 1px solid var(--divider);
  }
  .stepper svg { display: block; }
  .step-number {
    font-family: "Roboto", Arial, sans-serif;
    font-size: 10px; font-weight: 500; fill: var(--step-idle-text);
  }

  .page-title {
    position: absolute; top: 80px; left: 0; width: 1200px;
    text-align: center;
    font-size: 15px; font-weight: 300; letter-spacing: 0.3px;
    color: var(--title);
  }

  .call-card {
    position: absolute; left: 290px; top: 146px; width: 620px; height: 408px;
    background: var(--surface);
    border-radius: 8px;
    box-shadow: 0 4px 18px rgba(40, 60, 110, 0.06);
  }
  .brand-name {
    position: absolute; left: 17px; top: 16px;
    font-size: 15px; font-weight: 500; letter-spacing: 0.4px;
    color: var(--brand);
  }
  .call-message {
    position: absolute; left: 70px; top: 265px; width: 480px;
    text-align: center;
    font-size: 12.8px; font-weight: 400; line-height: 16px;
    color: var(--body-text);
  }
  .confirm-button {
    position: absolute; left: 228px; top: 328px; width: 166px; height: 36px;
    border: 1.5px solid var(--accent-soft); border-radius: 18px;
    background: var(--surface);
    font-family: "Roboto", Arial, sans-serif;
    font-size: 13.5px; font-weight: 400;
    color: var(--accent);
  }

  .page-footer {
    position: absolute; top: 594px; left: 0; width: 1200px;
    text-align: center;
    font-size: 9px; color: var(--footer-text);
  }
</style>
</head>
<body>
<div class="screen">
  <header class="stepper">
    <svg width="1200" height="55" viewBox="0 0 1200 55" aria-label="Progress: step 1 of 10">
      <g stroke-width="1.2">
        <line x1="57" y1="28" x2="138" y2="28" stroke="var(--accent)"/>
        <line x1="169" y1="28" x2="250" y2="28" stroke="var(--step-idle)"/>
        <line x1="281" y1="28" x2="362" y2="28" stroke="var(--step-idle)"/>
        <line x1="393" y1="28" x2="474" y2="28" stroke="var(--step-idle)"/>
        <line x1="505" y1="28" x2="586" y2="28" stroke="var(--step-idle)"/>
        <line x1="617" y1="28" x2="698" y2="28" stroke="var(--step-idle)"/>
        <line x1="729" y1="28" x2="810" y2="28" stroke="var(--step-idle)"/>
        <line x1="841" y1="28" x2="922" y2="28" stroke="var(--step-idle)"/>
        <line x1="953" y1="28" x2="1034" y2="28" stroke="var(--step-idle)"/>
        <line x1="1065" y1="28" x2="1146" y2="28" stroke="var(--step-idle)"/>
      </g>
      <circle cx="41" cy="28" r="9" fill="var(--accent)"/>
      <circle cx="153" cy="28" r="9" fill="var(--step-idle)"/>
      <circle cx="265" cy="28" r="9" fill="var(--step-idle)"/>
      <circle cx="377" cy="28" r="9" fill="var(--step-idle)"/>
      <circle cx="489" cy="28" r="9" fill="var(--step-idle)"/>
      <circle cx="601" cy="28" r="9" fill="var(--step-idle)"/>
      <circle cx="713" cy="28" r="9" fill="var(--step-idle)"/>
      <circle cx="825" cy="28" r="9" fill="var(--step-idle)"/>
      <circle cx="937" cy="28" r="9" fill="var(--step-idle)"/>
      <circle cx="1049" cy="28" r="9" fill="var(--step-idle)"/>
      <circle cx="1161" cy="28" r="9" fill="var(--step-idle)"/>
      <g class="step-number" text-anchor="middle">
        <text x="41" y="31.5">1</text>
        <text x="153" y="31.5">2</text>
        <text x="265" y="31.5">3</text>
        <text x="377" y="31.5">4</text>
        <text x="489" y="31.5">5</text>
        <text x="601" y="31.5">6</text>
        <text x="713" y="31.5">7</text>
        <text x="825" y="31.5">8</text>
        <text x="937" y="31.5">9</text>
        <text x="1049" y="31.5">10</text>
      </g>
      <g fill="none" stroke="#ffffff" stroke-width="1.1" stroke-linejoin="round">
        <line x1="1157" y1="23" x2="1157" y2="33"/>
        <path d="M1157 23.5 H1165 L1163 26 L1165 28.5 H1157"/>
      </g>
    </svg>
  </header>

  <h1 class="page-title">WAITING FOR OPERATOR</h1>

  <main class="call-card">
    <div class="brand-name">NOVIA BANK</div>
    <p class="call-message">The operator is ready to start your video identification. Please click on continue to start the process</p>
    <button class="confirm-button" type="button">Confirm</button>
  </main>

  <footer class="page-footer">©2019 NOVIA BANK</footer>
</div>
</body>
</html>
```